New cool to-go cup for KELMO Coffee

UPDATE MARCH 18: Please read the attached document "Design ideas - Front" with a mock-up of the design we are looking for. And please don't change the logo.

We are looking for a new cool design for our to-go cups in kraft paper (same style as the attached photo).

The idea:

We have three different cups sizes: 6oz, 8oz and 12oz. We call them “Tiny-Lark” (6oz), “Mid-Wren” (8oz) and “Tall-heron” (12oz) (refers to the size in milliliters). We would like to include this in the cup design. Please see the attached sketch of the idea ("Design ideas - Front").

The backside of the cup should have the attached text and logo ("Design ideas - Back").

But other ideas are also very welcome too! Maybe just a simple cup with the logo.

Please keep the design very minimalistic. The more simple the better.

Target Market(s)

Young urban people

Industry/Entity Type

Coffee shop

Font styles to use
Sans Serif

Requirements
Must have
• Kraft paper cups

```html
<!DOCTYPE html>
<html lang="en">
<head>
<meta charset="utf-8">
<title>KELMO Coffee – to-go cup range</title>
<link rel="stylesheet" href="https://fonts.googleapis.com/css2?family=Open+Sans:wght@400;600&display=swap">
<style>
  :root {
    --backdrop: #ececea;
    --kraft: #c2955f;
    --ink: #5a3419;
    --cup-white: #f7f7f5;
    --rim-edge: #dcdcd8;
  }
  html, body {
    margin: 0;
    padding: 0;
    overflow: hidden;
    background: var(--backdrop);
  }
  .canvas {
    width: 1200px;
    height: 675px;
    overflow: hidden;
    background: var(--backdrop);
  }
  .cup-rim, .cup-base { fill: var(--cup-white); stroke: var(--rim-edge); stroke-width: 1; }
  .cup-wrap { fill: var(--kraft); }
  .brand-dot { fill: none; stroke: var(--ink); stroke-width: 2; }
  .brand-name {
    font-family: "Open Sans", sans-serif;
    font-weight: 600;
    font-size: 13px;
    fill: var(--ink);
  }
  .size-name {
    font-family: "Open Sans", sans-serif;
    font-weight: 400;
    fill: var(--ink);
  }
</style>
</head>
<body>
<div class="canvas">
  <svg width="1200" height="675" viewBox="0 0 1200 675" xmlns="http://www.w3.org/2000/svg">

    <!-- Tiny-Lark cup -->
    <g class="cup cup-tiny">
      <polygon class="cup-wrap" points="201,303 399,303 384,490 216,490"/>
      <polygon class="cup-base" points="216,490 384,490 382,519 218,519"/>
      <polygon class="cup-rim" points="198,291 402,291 401,303 199,303"/>
      <g class="brand">
        <circle class="brand-dot" cx="256" cy="381" r="6"/>
        <text class="brand-name" x="267" y="386">KELMO Coffee</text>
      </g>
      <text class="size-name" x="300" y="455" font-size="31" text-anchor="middle">tinylark</text>
    </g>

    <!-- Mid-Wren cup -->
    <g class="cup cup-mid">
      <polygon class="cup-wrap" points="447,248 676,248 647,500 476,500"/>
      <polygon class="cup-base" points="476,500 647,500 643,534 480,534"/>
      <polygon class="cup-rim" points="443,234 680,234 679,248 444,248"/>
      <g class="brand">
        <circle class="brand-dot" cx="517" cy="344" r="6"/>
        <text class="brand-name" x="528" y="349">KELMO Coffee</text>
      </g>
      <text class="size-name" x="561" y="433" font-size="31" text-anchor="middle">#midwren</text>
    </g>

    <!-- Tall-heron cup -->
    <g class="cup cup-tall">
      <polygon class="cup-wrap" points="730,205 995,205 959,505 766,505"/>
      <polygon class="cup-base" points="766,505 959,505 955,537 770,537"/>
      <polygon class="cup-rim" points="726,191 999,191 998,205 728,205"/>
      <g class="brand">
        <circle class="brand-dot" cx="818" cy="341" r="6"/>
        <text class="brand-name" x="829" y="346">KELMO Coffee</text>
      </g>
      <text class="size-name" x="862" y="422" font-size="37" text-anchor="middle">#tallheron</text>
    </g>

  </svg>
</div>
</body>
</html>
```